A website design for a consultation firm

We are located in Istanbul, Turkey and offers our consultation services to customers interested in investing in Realestate, Education and Investment particularly this coming from Arab world and English speaking countries.

The site should carry our message of deep knowledge about the Turkish markets in the mentioned sectors of interest, sincerity and keenness.

The final deliverable of the winning design should include:
- The source files of the final designs. e.g. AI, PSD ..etc
- The redline markup for the design using a Specctr or any other similar tool.

Target Market(s)

English and Arabic speaking countries with a Turkish theme since we are a Turkish company

Industry/Entity Type

Consulting

Number of Pages Required

2 page

Font styles to use
Sans Serif

Requirements
Must have
• The site should serve the following main sections:
• - Why QVD?
• - Reports & studies
• - Sectors
• - Our team
• - Contact
• We need a design that could be converted into a WordPress theme.
• The design should be in English but should accommodate other languages including RTL.
• You can use the color theme you like as long as it does't dissolve the logo.
• The site should link into our accounts on the following networks:
• - Twitter
• - Facebook
• - LinkedIn
• The design should be responsive and nicely rendered on Desktop, Tablets and Smart phones.
Nice to have
• The site would be nice to balance between being informative and

```html
<!DOCTYPE html>
<html lang="en">
<head>
<meta charset="utf-8">
<title>QVD Consulting</title>
<link href="https://fonts.googleapis.com/css2?family=Open+Sans:wght@400;600;700&display=swap" rel="stylesheet">
<style>
:root{
  --red:#c8202a;
  --navy:#1f3d78;
  --navy-dark:#16305f;
  --text:#333;
  --muted:#777;
  --rule:#dcdcdc;
  --panel:#f2f2f2;
  --dark:#3a3a3c;
  --footer:#262627;
  --social-a:#3b5fa8;
  --social-b:#2ea3e0;
  --social-c:#1f7bb6;
  --white:#fff;
}
*{box-sizing:border-box;margin:0;padding:0}
html,body{width:1200px;height:2348px;overflow:hidden}
body{font-family:"Open Sans",Arial,sans-serif;color:var(--text);background:var(--white);position:relative}
section,header,footer{position:absolute;left:0;width:1200px}

/* Header */
.site-header{top:0;height:88px;background:var(--white);border-bottom:1px solid var(--rule)}
.brand{position:absolute;left:100px;top:22px;display:flex;align-items:center;gap:10px}
.brand-dot{width:40px;height:40px;border-radius:50%;background:var(--navy)}
.brand-name{font-size:30px;font-weight:700;color:var(--navy);letter-spacing:1px}
.main-nav{position:absolute;left:352px;top:0;height:88px;display:flex;align-items:center}
.main-nav a{display:block;padding:0 22px;height:88px;line-height:88px;font-size:15px;color:var(--text);text-decoration:none;position:relative}
.main-nav a.active{color:var(--red)}
.main-nav a.active::after{content:"";position:absolute;left:14px;right:14px;bottom:22px;height:2px;background:var(--red)}
.search-icon{position:absolute;left:1046px;top:32px}

/* Hero */
.hero{top:88px;height:504px}
.hero-photo{position:absolute;inset:0;background:linear-gradient(180deg,#cfd4da 0%,#8e97a3 45%,#3e4a5c 100%)}
.hero-title{position:absolute;left:0;right:0;top:200px;text-align:center;color:var(--white);font-weight:700;line-height:1}
.hero-title .accent{display:block;color:var(--red);font-size:38px}
.hero-title .word{display:block;font-size:58px;letter-spacing:2px;margin-top:4px}

/* Services */
.services{top:592px;height:436px;text-align:center}
.section-title{font-size:34px;font-weight:400;color:var(--text)}
.services .section-title{margin-top:38px}
.section-lead{font-size:15px;color:var(--muted);line-height:22px;margin-top:10px}
.service-list{position:absolute;top:176px;left:140px;width:920px;display:flex;justify-content:space-between}
.service{width:250px}
.service-icon{width:110px;height:110px;margin:0 auto;display:block}
.service h3{font-size:22px;font-weight:400;margin-top:18px}
.service p{font-size:13px;color:var(--muted);line-height:19px;margin-top:8px}

/* About / Why */
.about-why{top:1028px;height:332px;border-top:1px solid var(--rule)}
.col-title{font-size:32px;font-weight:600;color:var(--text);position:relative;padding-top:18px}
.col-title::before{content:"";position:absolute;left:0;top:0;width:48px;height:5px;background:var(--navy)}
.about{position:absolute;left:104px;top:56px;width:600px}
.about .col-title{border-bottom:1px solid var(--rule);padding-bottom:12px}
.about p{font-size:13px;line-height:20px;color:var(--muted);margin-top:14px}
.why{position:absolute;left:764px;top:56px;width:336px}
.why .col-title{padding-bottom:12px}
.why ul{list-style:none;margin-top:6px}
.why li{display:flex;align-items:center;gap:18px;height:44px;border-bottom:1px solid var(--rule);font-size:13px;color:var(--muted)}
.tick{width:22px;height:22px;flex:none;display:block}

/* Recent posts */
.recent{top:1360px;height:520px;background:var(--panel);text-align:center}
.recent .section-title{margin-top:30px}
.post-grid{position:absolute;left:104px;top:112px;width:1044px;display:grid;grid-template-columns:488px 528px;column-gap:28px;row-gap:38px}
.post{height:164px;background:var(--white);border:1px solid #d4d4d4;box-shadow:0 1px 4px rgba(0,0,0,.12);display:flex;text-align:left;padding:10px}
.post-photo{width:200px;height:142px;flex:none;background:linear-gradient(135deg,#b9c3cf,#5d6c80)}
.post-body{padding:6px 0 0 20px}
.post-body h4{font-size:18px;font-weight:700;color:var(--text)}
.post-body time{display:block;font-size:12px;color:var(--muted);margin-top:4px}
.post-body p{font-size:12px;line-height:18px;color:var(--muted);margin-top:8px}

/* Contact */
.contact{top:1880px;height:420px;color:var(--white);text-align:center}
.contact-bg{position:absolute;inset:0;background:linear-gradient(180deg,#4a4a4c,#2f2f31)}
.contact-inner{position:relative}
.contact .section-title{color:var(--white);margin-top:38px}
.contact .section-lead{color:#cfcfcf}
.contact-items{position:absolute;top:160px;left:100px;width:1000px;display:flex;justify-content:space-between}
.contact-item{width:300px}
.contact-item svg{display:block;margin:0 auto}
.contact-item p{font-size:13px;line-height:19px;margin-top:18px;color:#e6e6e6}
.contact-item .phone{font-size:18px}
.social{position:absolute;top:334px;left:0;right:0;display:flex;justify-content:center;gap:10px}
.social a{display:block;width:34px;height:34px;border-radius:50%}
.social a:nth-child(1){background:var(--social-a)}
.social a:nth-child(2){background:var(--social-b)}
.social a:nth-child(3){background:var(--social-c)}

/* Footer */
.site-footer{top:2300px;height:48px;background:var(--footer);color:#9a9a9a;font-size:12px;text-align:center;line-height:48px}
</style>
</head>
<body>

<header class="site-header">
  <div class="brand"><span class="brand-dot"></span><span class="brand-name">QVD</span></div>
  <nav class="main-nav">
    <a class="active" href="#">Home</a>
    <a href="#">Why QVD?</a>
    <a href="#">Reports &amp; studies</a>
    <a href="#">Sectors</a>
    <a href="#">Our team</a>
    <a href="#">Contact</a>
  </nav>
  <svg class="search-icon" width="22" height="22" viewBox="0 0 22 22"><circle cx="9" cy="9" r="7" fill="none" stroke="#444" stroke-width="2.4"/><line x1="14" y1="14" x2="20" y2="20" stroke="#444" stroke-width="2.6" stroke-linecap="round"/></svg>
</header>

<section class="hero">
  <div class="hero-photo" role="img" aria-label="Business people in suits shaking hands in a bright office"></div>
  <h1 class="hero-title"><span class="accent">QVD</span><span class="word">CONSULTING</span></h1>
</section>

<section class="services">
  <h2 class="section-title">Our Services</h2>
  <p class="section-lead">Lorem ipsum dolor sit amet, consectetur adipiscing elit, sed diam nonumy eirmod tempor.<br>Lorem ipsum dolor sit amet, consectetur adipiscing elit.</p>
  <div class="service-list">
    <div class="service">
      <svg class="service-icon" viewBox="0 0 110 110"><circle cx="55" cy="55" r="53" fill="var(--navy)"/><circle cx="55" cy="55" r="45" fill="none" stroke="#fff" stroke-width="3"/><circle cx="55" cy="55" r="18" fill="none" stroke="#fff" stroke-width="4"/><circle cx="55" cy="55" r="8" fill="none" stroke="#fff" stroke-width="4"/><line x1="55" y1="55" x2="74" y2="36" stroke="#fff" stroke-width="4" stroke-linecap="round"/></svg>
      <h3>Strategy</h3>
      <p>Lorem ipsum dolor sit amet, consectetur adipiscing elit, sed diam nonumy eirmod. Lorem ipsum dolor</p>
    </div>
    <div class="service">
      <svg class="service-icon" viewBox="0 0 110 110"><circle cx="55" cy="55" r="53" fill="var(--navy)"/><circle cx="55" cy="55" r="45" fill="none" stroke="#fff" stroke-width="3"/><circle cx="47" cy="60" r="13" fill="none" stroke="#fff" stroke-width="6" stroke-dasharray="5 3"/><circle cx="47" cy="60" r="4" fill="#fff"/><circle cx="66" cy="42" r="9" fill="none" stroke="#fff" stroke-width="5" stroke-dasharray="4 3"/></svg>
      <h3>Technology</h3>
      <p>Lorem ipsum dolor sit amet, consectetur adipiscing elit, sed diam nonumy eirmod. Lorem ipsum dolor</p>
    </div>
    <div class="service">
      <svg class="service-icon" viewBox="0 0 110 110"><circle cx="55" cy="55" r="53" fill="var(--navy)"/><circle cx="55" cy="55" r="45" fill="none" stroke="#fff" stroke-width="3"/><circle cx="50" cy="58" r="14" fill="none" stroke="#fff" stroke-width="7" stroke-dasharray="5 3"/><circle cx="70" cy="40" r="8" fill="none" stroke="#fff" stroke-width="5" stroke-dasharray="4 3"/></svg>
      <h3>Operation</h3>
      <p>Lorem ipsum dolor sit amet, consectetur adipiscing elit, sed diam nonumy eirmod. Lorem ipsum dolor</p>
    </div>
  </div>
</section>

<section class="about-why">
  <div class="about">
    <h2 class="col-title">About QVD</h2>
    <p>Lorem ipsum dolor sit amet, consectetur adipiscing elit, sed diam nonumy eirmod tempor. Lorem ipsum dolor sit amet, consectetur adipiscing elit sed diam nonumy eirmod tempor. Lorem ipsum dolor sit amet, consectetur adipiscing elit, sed diam nonumy eirmod tempor.</p>
    <p>Lorem ipsum dolor sit amet, consectetur adipiscing elit, sed diam nonumy eirmod tempor.</p>
  </div>
  <div class="why">
    <h2 class="col-title">Why Work With Us</h2>
    <ul>
      <li><svg class="tick" viewBox="0 0 22 22"><rect width="22" height="22" fill="var(--text)"/><polyline points="5,11 9,15 17,6" fill="none" stroke="#fff" stroke-width="2.6"/></svg>Lorem ipsum dolor sit amet, consectetur</li>
      <li><svg class="tick" viewBox="0 0 22 22"><rect width="22" height="22" fill="var(--text)"/><polyline points="5,11 9,15 17,6" fill="none" stroke="#fff" stroke-width="2.6"/></svg>Lorem ipsum dolor sit amet, consectetur</li>
      <li><svg class="tick" viewBox="0 0 22 22"><rect width="22" height="22" fill="var(--text)"/><polyline points="5,11 9,15 17,6" fill="none" stroke="#fff" stroke-width="2.6"/></svg>Lorem ipsum dolor sit amet, consectetur</li>
    </ul>
  </div>
</section>

<section class="recent">
  <h2 class="section-title">Recent Post</h2>
  <div class="post-grid">
    <article class="post">
      <div class="post-photo" role="img" aria-label="Colleagues meeting around a laptop"></div>
      <div class="post-body"><h4>Lorem ipsum dolor site</h4><time>June 20, 2015</time><p>Lorem ipsum dolor sit amet, consectetur adipiscing elit, sed diam nonumy. Aenean commodo ligula eget dolor.</p></div>
    </article>
    <article class="post">
      <div class="post-photo" role="img" aria-label="Business team reviewing documents at a desk"></div>
      <div class="post-body"><h4>Lorem ipsum dolor site</h4><time>June 20, 2015</time><p>Lorem ipsum dolor sit amet, consectetur adipiscing elit, sed diam nonumy. Aenean commodo ligula eget dolor.</p></div>
    </article>
    <article class="post">
      <div class="post-photo" role="img" aria-label="Consultants talking in a modern office"></div>
      <div class="post-body"><h4>Lorem ipsum dolor site</h4><time>June 20, 2015</time><p>Lorem ipsum dolor sit amet, consectetur adipiscing elit, sed diam nonumy. Aenean commodo ligula eget dolor.</p></div>
    </article>
    <article class="post">
      <div class="post-photo" role="img" aria-label="Hands typing on a laptop keyboard"></div>
      <div class="post-body"><h4>Lorem ipsum dolor site</h4><time>June 20, 2015</time><p>Lorem ipsum dolor sit amet, consectetur adipiscing elit, sed diam nonumy. Aenean commodo ligula eget dolor.</p></div>
    </article>
  </div>
</section>

<section class="contact">
  <div class="contact-bg" role="img" aria-label="Dimmed photo of a business desk with a laptop"></div>
  <div class="contact-inner">
    <h2 class="section-title">Contact Info</h2>
    <p class="section-lead">Lorem ipsum dolor sit amet, consectetur adipiscing elit, sed diam nonumy eirmod tempor.</p>
    <div class="contact-items">
      <div class="contact-item">
        <svg width="56" height="56" viewBox="0 0 56 56"><circle cx="28" cy="28" r="27" fill="#fff"/><path d="M28 14a9 9 0 0 0-9 9c0 7 9 18 9 18s9-11 9-18a9 9 0 0 0-9-9z" fill="var(--dark)"/><circle cx="28" cy="23" r="3.5" fill="#fff"/></svg>
        <p>Lorem ipsum dolor sit amet<br>Lorem consectetur adipiscing elit</p>
      </div>
      <div class="contact-item">
        <svg width="56" height="56" viewBox="0 0 56 56"><circle cx="28" cy="28" r="26" fill="none" stroke="#fff" stroke-width="2"/><path d="M21 17l5 5-3 4c2 4 5 7 9 9l4-3 5 5-4 4c-10-1-19-10-20-20z" fill="#fff"/></svg>
        <p class="phone">(123) 456 - 7890</p>
      </div>
      <div class="contact-item">
        <svg width="56" height="56" viewBox="0 0 56 56"><circle cx="28" cy="28" r="26" fill="none" stroke="#fff" stroke-width="2"/><rect x="16" y="20" width="24" height="16" fill="none" stroke="#fff" stroke-width="2.2"/><polyline points="16,20 28,30 40,20" fill="none" stroke="#fff" stroke-width="2.2"/></svg>
        <p>info@qvd.com</p>
      </div>
    </div>
    <div class="social">
      <a href="#" aria-label="Social profile one"></a>
      <a href="#" aria-label="Social profile two"></a>
      <a href="#" aria-label="Social profile three"></a>
    </div>
  </div>
</section>

<footer class="site-footer">Copyright © 2016 , All rights reserved.</footer>

</body>
</html>
```